Creation of an elegant and modern turnkey Shopify website

Hello,

We are a new company specializing in the sale of above-ground pools. We want to create a turnkey website, ideally using Shopify. For now, we need a "showcase" site, not an e-commerce platform, with four tabs:

Home Page (an overall presentation of the company)
Our Products (an overview of all the above-ground pools we sell)
Our Projects (a page inspired by Snapgrid to showcase photos of our future projects)
Contact (a page with all our contact information and a contact form)

We are looking to create a highly visual, elegant, and modern website with vibrant splashes of color. We will provide the text, photos (along with instructions on where to place them on each page), and all other necessary information as attachments.

Thank you in advance for your proposals!

The Brisa Lagoon Team

Target Market(s)

Targeted at Swiss customers (a translator will need to be installed for different languages)

Industry/Entity Type

Sale of customised above-ground pools

Coding

Coded - Design and coding required

Font styles to use
Sans Serif

Colors
0094D4
00A9DD
6FCCEA
C7EBF8
E9F6FB
00AB8E
00BBA5
67D7C9
C6EFE9
E9F9F6

Requirements
Must have
• A stunning, elegant and modern look
Nice to have
• Inspiration from the colors of our logo throughout the site, but in an elegant way
Should not have
• An overly classic look for swimming pool sites

```html
<!DOCTYPE html>
<html lang="en">
<head>
<meta charset="UTF-8">
<title>Brisa Lagoon – Premium Above-Ground Pools</title>
<link href="https://fonts.googleapis.com/css2?family=Poiret+One&family=Roboto:wght@300;400;500;700&display=swap" rel="stylesheet">
<style>
:root{
  --cyan:#00D9F2;
  --cyan-deep:#00C4E0;
  --water:#35D3EE;
  --water-light:#8FE6F5;
  --ice:#EEF9FD;
  --ink:#2A2A2A;
  --text:#444;
  --muted:#8A8A8A;
  --card:#F4F4F4;
  --band:#8C8C8C;
  --footer:#2B2B2B;
  --white:#FFFFFF;
}
*{box-sizing:border-box;margin:0;padding:0}
html,body{width:1200px;height:2528px;overflow:hidden}
body{position:relative;background:var(--white);font-family:'Roboto',sans-serif;color:var(--text)}
.abs{position:absolute}
.display{font-family:'Poiret One',sans-serif;color:var(--ink);letter-spacing:1px;font-weight:400}

/* header */
.site-header{left:0;top:0;width:1200px;height:72px;background:var(--white)}
.main-nav{left:122px;top:30px;display:flex;gap:31px;font-size:12.5px;color:#555;letter-spacing:.3px}
.brand-mark{left:540px;top:8px;width:120px;text-align:center;font-family:'Poiret One',sans-serif;font-size:22px;line-height:26px;color:var(--cyan-deep);letter-spacing:2px}
.search{left:703px;top:15px;width:276px;height:44px;border:1px solid #999;font-size:13px;color:#888;padding:13px 14px}
.search svg{position:absolute;right:12px;top:11px}
.account{left:992px;top:18px;width:36px;height:36px;border-radius:50%;background:#E6E6E6}
.account svg{position:absolute;left:9px;top:8px}
.lang{left:1045px;top:30px;font-size:12.5px;color:#666}

/* hero */
.hero{left:0;top:72px;width:1200px;height:506px;background:linear-gradient(135deg,var(--water) 0%,var(--water-light) 55%,var(--water) 100%);overflow:hidden}
.hero-logo{left:118px;top:52px;width:400px;font-family:'Poiret One',sans-serif;color:var(--white);font-size:88px;line-height:130px;letter-spacing:2px;white-space:nowrap}
.hero-tag{left:121px;top:338px;color:var(--white);font-size:21px;line-height:27px;font-weight:400}
.btn{display:flex;align-items:center;height:36px;font-size:12.5px;font-weight:500;letter-spacing:.2px}
.btn .label{padding:0 9px 0 12px;height:100%;display:flex;align-items:center}
.btn .arrow{width:36px;height:100%;border-left:1px solid currentColor;display:flex;align-items:center;justify-content:center}
.btn-white{background:var(--white);color:var(--ink)}
.btn-white .arrow{border-left-color:#333}
.btn-cyan{background:var(--cyan);color:var(--white)}
.btn-cyan .arrow{border-left-color:rgba(255,255,255,.8)}
.hero .btn{left:122px;top:406px}
.hero-ring{left:540px;top:36px;width:604px;height:410px;border:22px solid rgba(255,255,255,.35);border-radius:50%}
.hero-photo{left:622px;top:16px;width:448px;height:474px;border-radius:50%;border:6px solid var(--white);background:radial-gradient(circle at 50% 45%,#D6F3F9 0%,#B3E7F2 55%,#92DAEB 100%)}

/* intro */
.intro-title{left:120px;top:626px;font-size:31px;line-height:42px;width:430px}
.intro-btn{left:122px;top:762px}
.intro-text{left:704px;top:652px;width:380px;font-size:11.5px;line-height:18.2px;color:#444}
.intro-text p+p{margin-top:17px}

/* why */
.why-title{left:0;top:856px;width:1200px;text-align:center;font-size:30px}
.cards{left:122px;top:910px;display:flex;gap:12px}
.card{width:182px;height:218px;background:var(--card);text-align:center;padding-top:20px}
.card .ico{width:82px;height:92px;margin:0 auto;border:2px solid var(--cyan);border-radius:50%;display:flex;align-items:center;justify-content:center}
.card h3{font-weight:400;font-size:14.5px;color:#333;margin-top:11px}
.card p{font-size:9.8px;line-height:14.4px;color:#555;margin:6px 12px 0}
.card p.light{color:#A8A8A8}

/* personalized */
.pers-photo{left:0;top:1194px;width:644px;height:384px;background:linear-gradient(160deg,#9FDDEA 0%,#CBEFF5 40%,#8DD0DA 70%,#5AB5BE 100%)}
.pers-panel{left:644px;top:1194px;width:556px;height:384px;background:var(--ice)}
.pers-title{left:748px;top:1310px;font-size:30px}
.pers-text{left:751px;top:1352px;width:340px;font-size:11.5px;line-height:19px}
.pers-btn{left:753px;top:1442px}

/* guarantee */
.guar-title{left:120px;top:1708px;font-size:30px}
.guar-text{left:121px;top:1751px;width:350px;font-size:11.5px;line-height:19px}
.badge{left:122px;top:1840px;width:210px;height:84px}
.guar-ring{left:600px;top:1650px;width:500px;height:340px;border:22px solid #00E5F5;border-radius:50%}
.guar-photo{left:678px;top:1624px;width:340px;height:390px;border-radius:50%;border:10px solid #E2E2E2;background:linear-gradient(200deg,#5E93C9 0%,#A9C8E2 35%,#8FD6CC 60%,#2E8A78 100%)}

/* contact */
.contact{left:0;top:2075px;width:1200px;height:235px;background:var(--band)}
.contact-title{left:0;top:2116px;width:1200px;text-align:center;font-size:30px;color:var(--white)}
.contact-text{left:370px;top:2156px;width:460px;text-align:center;font-size:11.5px;line-height:19px;color:var(--white)}
.contact-btn{left:532px;top:2232px}

/* footer */
.footer{left:0;top:2310px;width:1200px;height:218px;background:var(--footer)}
.foot-logo{left:120px;top:2340px;font-family:'Poiret One',sans-serif;font-size:38px;line-height:48px;color:var(--cyan);letter-spacing:2px}
.foot-col h4{font-family:'Poiret One',sans-serif;font-weight:400;font-size:16px;color:var(--white);letter-spacing:1.5px;margin-bottom:14px}
.foot-col li{list-style:none;font-size:9.8px;color:#CFCFCF;margin-bottom:11px;display:flex;align-items:center;gap:6px}
.foot-col li i{display:inline-block;width:14px;height:14px;border:1px solid #CFCFCF;border-radius:50%}
.foot-col p{font-size:9.8px;line-height:17px;color:#CFCFCF;width:190px}
.divider{width:1px;height:146px;background:#666;top:2345px}
.newsletter{left:884px;top:2418px;width:194px;height:40px;background:var(--white);font-size:9.8px;color:#777;padding:14px 13px}
.newsletter span{position:absolute;right:0;top:0;width:40px;height:40px;border-left:1px solid #ccc;display:flex;align-items:center;justify-content:center}
.foot-rule{left:126px;top:2491px;width:952px;height:1px;background:#666}
.copyright{left:0;top:2502px;width:1200px;text-align:center;font-size:9.8px;color:#BBB}
</style>
</head>
<body>

<header class="abs site-header">
  <nav class="abs main-nav"><span>HOME</span><span>OUR PRODUCTS</span><span>OUR PROJECTS</span><span>CONTACT US</span></nav>
  <div class="abs brand-mark">BRISA<br>LAGOON</div>
  <div class="abs search">Search
    <svg width="20" height="20" viewBox="0 0 20 20" fill="none" stroke="#222" stroke-width="2"><circle cx="8.5" cy="8.5" r="6.5"/><path d="M13.5 13.5L18 18"/></svg>
  </div>
  <div class="abs account"><svg width="18" height="20" viewBox="0 0 18 20" fill="none" stroke="#444" stroke-width="1.4"><circle cx="9" cy="6" r="4"/><path d="M1.5 19c0-4 3.4-7 7.5-7s7.5 3 7.5 7"/></svg></div>
  <div class="abs lang">EN &#8964;</div>
</header>

<section class="abs hero">
  <div class="abs hero-ring"></div>
  <div class="abs hero-photo" role="img" aria-label="Aerial photo of a person floating on a pink ring in clear pool water"></div>
  <div class="abs hero-logo">BRISA<br>LAGOON</div>
  <div class="abs hero-tag">Transform Your Garden with Our<br>Premium Above-Ground Pools!</div>
  <div class="abs btn btn-white"><span class="label">GET STARTED</span><span class="arrow">&#10230;</span></div>
</section>

<section class="intro">
  <h1 class="abs display intro-title">TRANSFORM YOUR GARDEN WITH OUR PREMIUM ABOVE-GROUND POOLS!</h1>
  <div class="abs btn btn-cyan intro-btn"><span class="label">LEARN MORE</span><span class="arrow">&#10230;</span></div>
  <div class="abs intro-text">
    <p>Achieve your dreams with our custom, tailor-made above-ground pools.</p>
    <p>Imagine an exceptional relaxation and leisure space right in your own backyard. With our unparalleled expertise and commitment to excellence, we create above-ground pools that exceed all expectations. Our exclusive, custom-designed models are crafted to combine style, durability, and innovation, offering a unique and refined experience.</p>
  </div>
</section>

<section class="why">
  <h2 class="abs display why-title">WHY CHOOSE OUR ABOVE-GROUND POOLS?</h2>
  <div class="abs cards">
    <div class="card">
      <div class="ico"><svg width="40" height="40" viewBox="0 0 40 40" fill="none" stroke="#333" stroke-width="1.4"><circle cx="20" cy="16" r="11"/><path d="M20 10l2 4.5 4.8.5-3.6 3.2 1 4.8L20 20.6 15.8 23l1-4.8L13.2 15l4.8-.5z"/><path d="M13 25l-4 10 5-2 3 4 2-9M27 25l4 10-5-2-3 4-2-9"/></svg></div>
      <h3>Superior Quality</h3>
      <p>Each pool is constructed with high-quality materials, ensuring exceptional durability and strength.</p>
    </div>
    <div class="card">
      <div class="ico"><svg width="40" height="40" viewBox="0 0 40 40" fill="none" stroke="#333" stroke-width="1.4"><path d="M5 8v27h30"/><path d="M5 14h3M5 20h3M5 26h3M11 35v-3M17 35v-3M23 35v-3"/><path d="M14 27l16-16 3 3-16 16-4 1z"/><path d="M35 18v13H22z"/></svg></div>
      <h3>Elegant Design</h3>
      <p>Our pools come in a variety of styles and finishes, seamlessly blending into any garden setting.</p>
    </div>
    <div class="card">
      <div class="ico"><svg width="40" height="40" viewBox="0 0 40 40" fill="none" stroke="#333" stroke-width="1.4"><rect x="5" y="6" width="30" height="26" rx="2"/><path d="M5 12h30M10 18h14M10 23h10M10 28h8"/><circle cx="25" cy="9" r=".8"/><circle cx="29" cy="9" r=".8"/><path d="M24 22l9 4-4 1 3 4-2 1-3-4-2 3z"/></svg></div>
      <h3>Custom and Tailor-Made</h3>
      <p class="light">Create the pool of your dreams with our customization options, tailored to your specific tastes and needs.</p>
    </div>
    <div class="card">
      <div class="ico"><svg width="40" height="40" viewBox="0 0 40 40" fill="none" stroke="#333" stroke-width="1.4"><path d="M17 4h6l1 4 4 2 4-2 4 4-2 4 2 4 4 1v6l-4 1-2 4 2 4-4 4-4-2-4 2-1 4h-6l-1-4-4-2-4 2-4-4 2-4-2-4-4-1v-6l4-1 2-4-2-4 4-4 4 2 4-2z" transform="scale(.86) translate(3 3)"/><circle cx="20" cy="20" r="8"/><path d="M16 20l3 3 5-6"/></svg></div>
      <h3>Easy Installation</h3>
      <p>Enjoy your new oasis quickly with our simple and fast installation process.</p>
    </div>
    <div class="card">
      <div class="ico"><svg width="40" height="40" viewBox="0 0 40 40" fill="none" stroke="#333" stroke-width="1.4"><circle cx="20" cy="16" r="7"/><path d="M20 3v4M9 7l3 3M31 7l-3 3M6 16h4M30 16h4"/><path d="M17 23v12M23 23v12M14 28h12"/></svg></div>
      <h3>Constant Innovation</h3>
      <p class="light">We incorporate the latest technologies to provide you with an optimal and safe swimming experience.</p>
    </div>
  </div>
</section>

<section class="pers">
  <div class="abs pers-photo" role="img" aria-label="Photo of a person in a wide turquoise sun hat sitting by a pool over sparkling water"></div>
  <div class="abs pers-panel"></div>
  <h2 class="abs display pers-title">PERSONALIZED SERVICES</h2>
  <p class="abs pers-text">We understand that every garden and client is unique. That's why we offer personalized services, from design to installation and after-sales support. Our team of experts is here to answer all your questions and guide you throughout your project.</p>
  <div class="abs btn btn-cyan pers-btn"><span class="label">VIEW SERVICES</span><span class="arrow">&#10230;</span></div>
</section>

<section class="guar">
  <h2 class="abs display guar-title">GUARANTEED SATISFACTION</h2>
  <p class="abs guar-text">Your satisfaction is our top priority. We are committed to providing you with exceptional service and the highest quality products. Join our community of satisfied customers who are already enjoying their custom above-ground pools. 10-Year Warranty!</p>
  <svg class="abs badge" viewBox="0 0 210 84">
    <rect x="60" y="22" width="94" height="24" rx="12" fill="#6E6E6E"/>
    <rect x="60" y="46" width="148" height="24" rx="12" fill="#00D9F2"/>
    <circle cx="42" cy="42" r="41" fill="#E4E4E4"/>
    <circle cx="42" cy="42" r="35" fill="#00D9F2"/>
    <text x="42" y="52" text-anchor="middle" font-family="Roboto,sans-serif" font-weight="700" font-size="34" fill="#fff">10</text>
    <text x="92" y="41" font-family="Roboto,sans-serif" font-weight="700" font-size="17" fill="#fff">YEAR</text>
    <text x="86" y="65" font-family="Roboto,sans-serif" font-weight="700" font-size="17" fill="#fff">WARRANTY</text>
  </svg>
  <div class="abs guar-ring"></div>
  <div class="abs guar-photo" role="img" aria-label="Photo of a striped turquoise and white beach hut against a blue sky"></div>
</section>

<section class="contact-wrap">
  <div class="abs contact"></div>
  <h2 class="abs display contact-title">CONTACT US TODAY</h2>
  <p class="abs contact-text">Don't wait any longer to transform your garden into a wellness oasis. Contact us today to discover our range of customizable above-ground pools and get a tailored quote. Dive into a world of infinite possibilities with Brisa Lagoon</p>
  <div class="abs btn btn-cyan contact-btn"><span class="label">CONTACT US</span><span class="arrow">&#10230;</span></div>
</section>

<footer>
  <div class="abs footer"></div>
  <div class="abs foot-logo">BRISA<br>LAGOON</div>
  <div class="abs divider" style="left:338px"></div>
  <div class="abs foot-col" style="left:398px;top:2340px"><h4>QUICK LINKS</h4><ul><li>Home</li><li>Our Products</li><li>Our Projects</li><li>Contact Us</li></ul></div>
  <div class="abs divider" style="left:573px"></div>
  <div class="abs foot-col" style="left:664px;top:2340px"><h4>FOLLOW US</h4><ul><li><i></i>Pulse</li><li><i></i>Reelcast</li><li><i></i>Snapgrid</li><li><i></i>Chirper</li></ul></div>
  <div class="abs divider" style="left:827px"></div>
  <div class="abs foot-col" style="left:884px;top:2340px"><h4>SUBSCRIBE NEWSLETTER</h4><p>Lorem Ipsum is simply dummy text of the printing and typesetting industry.</p></div>
  <div class="abs newsletter">Enter Your Emai address<span>&#10230;</span></div>
  <div class="abs foot-rule"></div>
  <div class="abs copyright">© 2024 Brisa Lagoon All Rights Reserved</div>
</footer>

</body>
</html>
```